Contemporary update for a market leader in foodservice distribution

KORVELT is a market leader in foodservice distribution nationwide.
We have recently adopted a new look and feel for our flagship foodservice rewards programme, and we're looking to have our business cards reflect our new aesthetic. Below is a link to our new rewards website to give you a general idea on the look we're after. https://korveltperks.com.au/

Industry/Entity Type

Distribution

Contact Information for Business Card

Must have space for contact name, position, company name and ABN, address, phone number and direct number, fax, email, and web address.

Font styles to use
Serif
Sans Serif

Requirements
Must have
• We'd like a landscape design, with our 'Tip of the Peak' logo incorporated on either the front or the back of the card. The overall design should be contemporary and professional.
Nice to have
• I have included both the full colour and white version of our company logo - our preference is to have the company logo one solid colour (white, or a shade of grey) although we're also open to designs including the full colour logo. If you are able to incorporate a small Facebook and LinkedIn logo, please do so.
Should not have
• Should not have an over-complicated design. No images of globes, or food.

```html
<!DOCTYPE html>
<html lang="en">
<head>
<meta charset="utf-8">
<title>KORVELT Business Card</title>
<link href="https://fonts.googleapis.com/css2?family=Montserrat:wght@400;500;700;800&family=Libre+Baskerville&display=swap" rel="stylesheet">
<style>
  :root {
    --page-bg: #e4e6e8;
    --card-white: #ffffff;
    --brand-green: #0f8f5c;
    --accent-yellow: #f5e21c;
    --ink: #1d1d1b;
    --rule-black: #111111;
    --soft-text: #ffffff;
  }
  * { margin: 0; padding: 0; box-sizing: border-box; }
  html, body {
    width: 1200px; height: 900px; overflow: hidden;
    background: var(--page-bg);
    font-family: "Montserrat", Arial, sans-serif;
  }
  .card {
    position: absolute; left: 290px;
    width: 620px; height: 354px;
    border-radius: 26px; overflow: hidden;
    background: var(--card-white);
    box-shadow: 0 10px 28px rgba(0,0,0,0.18);
  }
  .card-front { top: 48px; }
  .card-back { top: 474px; }

  /* Front */
  .front-brand {
    position: absolute; left: 0; right: 0; top: 120px;
    display: flex; align-items: center; justify-content: center; gap: 16px;
  }
  .front-brand-dot {
    width: 46px; height: 46px; border-radius: 50%;
    background: var(--brand-green);
  }
  .front-brand-name {
    font-weight: 800; font-size: 54px; color: var(--ink);
    letter-spacing: -1px;
  }
  .front-web {
    position: absolute; left: 0; right: 0; top: 228px;
    text-align: center; font-size: 21px; color: var(--ink);
    letter-spacing: 0.5px;
  }

  /* Back */
  .back-shape { position: absolute; inset: 0; }
  .company-block {
    position: absolute; left: 118px; top: 44px;
    display: flex; align-items: center; gap: 16px;
  }
  .company-dot {
    width: 62px; height: 62px; border-radius: 50%;
    background: var(--brand-green);
  }
  .company-name {
    font-family: "Libre Baskerville", "Times New Roman", serif;
    font-size: 50px; color: var(--ink); line-height: 1; letter-spacing: 1px;
  }
  .company-tagline {
    font-size: 9.5px; font-weight: 700; color: var(--ink);
    letter-spacing: 0.4px; margin-top: 8px;
  }
  .company-abn { font-size: 14px; color: var(--ink); margin-top: 4px; }
  .company-abn span { color: var(--brand-green); }

  .person {
    position: absolute; left: 30px; top: 226px; width: 300px;
    text-align: right; color: var(--soft-text);
  }
  .person-name {
    font-weight: 800; font-size: 27px; color: var(--accent-yellow);
    letter-spacing: 0.5px; line-height: 1.05;
  }
  .person-role { font-size: 14px; letter-spacing: 0.5px; margin-top: 2px; }
  .person-address { font-size: 13.5px; line-height: 1.45; margin-top: 8px; }

  .contact-list {
    position: absolute; left: 350px; top: 178px;
    list-style: none; color: var(--soft-text);
    font-size: 13.5px; line-height: 1;
  }
  .contact-list li { display: flex; align-items: center; gap: 8px; height: 21px; }
  .contact-icon { width: 12px; height: 12px; flex: none; }
</style>
</head>
<body>

<section class="card card-front">
  <div class="front-brand">
    <div class="front-brand-dot"></div>
    <div class="front-brand-name">Tip of the Peak</div>
  </div>
  <div class="front-web">www.tipofthepeak.com</div>
</section>

<section class="card card-back">
  <svg class="back-shape" width="620" height="354" viewBox="0 0 620 354">
    <path d="M0,226 C210,214 430,186 620,98 L620,354 L0,354 Z" fill="var(--brand-green)"/>
    <path d="M0,222 C210,210 430,182 620,94" fill="none" stroke="var(--rule-black)" stroke-width="5"/>
  </svg>

  <div class="company-block">
    <div class="company-dot"></div>
    <div>
      <div class="company-name">KORVELT</div>
      <div class="company-tagline">AUSTRALIAN FOODSERVICE DISTRIBUTION</div>
      <div class="company-abn"><span>ABN:</span> 318 4621 0957</div>
    </div>
  </div>

  <div class="person">
    <div class="person-name">MARLO HENDRICKS</div>
    <div class="person-role">DIRECTOR</div>
    <div class="person-address">48 Ridgeway Lane<br>Harbourview NSW AUSTRALIA</div>
  </div>

  <ul class="contact-list">
    <li>
      <svg class="contact-icon" viewBox="0 0 12 12"><path d="M2,1 L4.5,1 L5.5,3.5 L4,4.5 C4.8,6.2 5.8,7.2 7.5,8 L8.5,6.5 L11,7.5 L11,10 C6,10.5 1.5,6 2,1 Z" fill="var(--accent-yellow)"/></svg>
      +61 2 5550 1184
    </li>
    <li>
      <svg class="contact-icon" viewBox="0 0 12 12"><rect x="3" y="0.5" width="6" height="11" rx="1.2" fill="var(--accent-yellow)"/><rect x="4.2" y="2" width="3.6" height="6.5" fill="var(--brand-green)"/></svg>
      +61 2 5550 1190 (Direct)
    </li>
    <li>
      <svg class="contact-icon" viewBox="0 0 12 12"><rect x="3" y="0.5" width="6" height="4" fill="var(--accent-yellow)"/><rect x="0.5" y="4.5" width="11" height="5" rx="1" fill="var(--accent-yellow)"/><rect x="3" y="8" width="6" height="3.5" fill="var(--accent-yellow)"/></svg>
      +61 2 5550 1127
    </li>
    <li>
      <svg class="contact-icon" viewBox="0 0 12 12"><rect x="0.5" y="2" width="11" height="8" rx="1" fill="var(--accent-yellow)"/><path d="M1,2.5 L6,6.5 L11,2.5" fill="none" stroke="var(--brand-green)" stroke-width="1.2"/></svg>
      info@tipofthepeak.com
    </li>
    <li>
      <svg class="contact-icon" viewBox="0 0 12 12"><circle cx="6" cy="6" r="5.5" fill="var(--accent-yellow)"/><path d="M0.5,6 H11.5 M6,0.5 V11.5" stroke="var(--brand-green)" stroke-width="1"/></svg>
      www.tipofthepeak.com
    </li>
  </ul>
</section>

</body>
</html>
```